Flyer-Design für Organisation von Golf Short Trips
Wir organisieren Golf Short Trips für Golfer aller Altersklassen. Hierfür sind wir auf der Suche nach einem minimalistischem und gleichzeitig hochwertigen Flyer/ Broschüre welches unsere wesentlichen Merkmale verkörpert.
Wir sind ein junges Unternehmen welches sich durch folgende Eigenschaften am besten beschreiben lässt: Innovativ, Disruptiv, Exklusiv, Produktiv, Modern. Diese Unternehmensphilosophie soll durch unseren Flyer erkennbar werden.
We organize golf short trips for golfers of all ages. For this we are looking for a minimalist and at the same time high quality flyer/ broschure which embodies our essential characteristics.
We are a young company which can be best described by the following characteristics: Innovative, Disruptive, Exclusive, Productive, Modern. This corporate philosophy should be recognizable through our flyer.
If possible use:
GRAU: #a2a4aa
GRÜN: #002F01
(SENFGELB: #cfa600)
Format: 138 x 297 / Two Pages (front/back)
So far, we have been working mainly with the Open Sans font.
Underground also Playfair styles. However, we would be happy to receive suggestions from you regarding the fonts.
!!! Please take the text specifications from the attached template: -> flyer_din_a5_hoch_tiefgruen.de.jpeg !!!
The design in general can be created by the designer at his own discretion.
A total of 3 logos must be included in the flyer. That of our company (medium size), the hotel group (small) and the golf course (small).
A small profile picture of the respective trainer should be placed on the front.
All textual content can be accessed via the following link: https://notizwerk-example.net/dokument/7Qx3LmRt9VbWz2KcHnPa5YsEu8JdGfTo4iXkNrBq/edit?usp=sharing

```html
<!DOCTYPE html>
<html lang="de">
<head>
<meta charset="utf-8">
<title>Golf Short Trip – Flyer</title>
<link rel="stylesheet" href="https://fonts.googleapis.com/css2?family=Montserrat:wght@300;400;500;700;800;900&display=swap">
<style>
  :root{
    --green:#13321a;
    --green-deep:#002f01;
    --gold:#cfa600;
    --grey:#a2a4aa;
    --grey-light:#d4d5d8;
    --field:#f0f0f2;
    --text:#1c1c1c;
  }
  *{box-sizing:border-box;margin:0;padding:0}
  html,body{width:1200px;height:2400px;overflow:hidden}
  body{background:linear-gradient(#cfcfd1,#f4f4f5 70%,#ffffff);font-family:"Montserrat",sans-serif;color:var(--text);position:relative}

  .flyer{position:absolute;left:100px;top:496px;width:1000px;height:1408px;background:#fff;overflow:hidden;box-shadow:0 4px 18px rgba(0,0,0,.12)}

  .bonus-badge{position:absolute;left:43px;top:54px;width:184px;height:184px;border-radius:50%;background:var(--green)}

  .club-panel{position:absolute;left:353px;top:0;width:285px;height:303px;background:var(--grey-light);display:flex;flex-direction:column;align-items:center;justify-content:center;gap:14px}
  .club-panel__mark{width:54px;height:54px;border-radius:50%;background:var(--green-deep)}
  .club-panel__name{font-weight:700;font-size:22px;letter-spacing:.28em;color:var(--green-deep);text-transform:uppercase;text-align:center;line-height:1.35}

  .club-title{position:absolute;left:0;top:344px;width:100%;text-align:center;font-weight:400;font-size:25px;letter-spacing:.62em;padding-left:.62em;color:#8f9196;line-height:33px;text-transform:uppercase;z-index:2}

  .course-photo{position:absolute;left:0;top:420px;width:100%;height:410px;overflow:hidden;
    background:
      linear-gradient(to bottom,#ffffff 0%,rgba(255,255,255,0) 26%),
      linear-gradient(to right,rgba(197,168,120,.9) 0%,rgba(197,168,120,0) 42%),
      linear-gradient(to bottom,#dfe6d2 22%,#9fbf6a 45%,#6f9a3a 68%,#53792b 100%)}
  .course-photo__word{position:absolute;left:56px;bottom:-50px;font-weight:900;font-size:306px;letter-spacing:-.02em;color:rgba(255,255,255,.62);line-height:1}

  .trip-band{position:absolute;left:0;top:829px;width:100%;height:122px;background:var(--green);border-top:4px solid #fff}
  .trip-band::before{content:"";position:absolute;left:0;right:0;top:4px;height:2px;background:rgba(255,255,255,.8)}
  .trip-band__title{position:absolute;left:0;right:0;top:30px;text-align:center;color:#fff;font-weight:900;font-size:58px;letter-spacing:.42em;padding-left:.42em;line-height:1}
  .trip-band__rule{position:absolute;left:0;right:0;bottom:-14px;height:10px;background:var(--gold);border-top:3px solid #fff}

  .dates{position:absolute;left:69px;top:1000px;width:868px}
  .dates__row{position:relative;height:70px}
  .dates__label{font-size:25px;line-height:25px;text-transform:uppercase;font-weight:400}
  .dates__label strong{display:block;font-weight:800}
  .dates__label--early strong{color:var(--gold)}
  .dates__label--second strong{color:var(--green)}
  .dates__field{position:absolute;right:0;top:4px;height:46px;background:var(--field)}
  .dates__row:first-child .dates__field{left:198px}
  .dates__row:last-child .dates__field{left:287px}

  .testimonial{position:absolute;left:106px;top:1197px;width:641px;height:120px;border:1.5px solid var(--grey);border-right:none;padding:20px 30px 0 33px;text-align:right}
  .testimonial__marks{position:absolute;left:-44px;top:-20px;width:56px;height:44px}
  .testimonial__quote{font-size:26px;font-weight:400;letter-spacing:.02em;white-space:nowrap}
  .testimonial__cite{display:block;margin-top:14px;font-style:normal;font-size:20px;letter-spacing:.03em}
  .testimonial__cite strong{font-weight:800;color:var(--green);margin-right:10px}
  .testimonial__cite span{border-left:1.5px solid var(--text);padding-left:8px}

  .trainer-photo{position:absolute;left:730px;top:1176px;width:206px;height:206px;border-radius:50%;background:radial-gradient(circle at 50% 45%,#d9d9d9,#9a9a9a 70%,#6e6e6e)}

  .footer-bar{position:absolute;left:353px;top:1377px;width:285px;height:31px;background:var(--gold)}
</style>
</head>
<body>
<main class="flyer">
  <div class="bonus-badge" role="img" aria-label="Frühbucher-Siegel"></div>

  <div class="club-panel">
    <div class="club-panel__mark"></div>
    <div class="club-panel__name">Alzette<br>Country Club</div>
  </div>

  <p class="club-title">Golf &amp; Country<br>Alzette Luxembourg</p>

  <div class="course-photo" role="img" aria-label="Foto eines Golfplatzes im Morgennebel mit Sandbunker und grünen Fairways">
    <span class="course-photo__word">GOLF</span>
  </div>

  <div class="trip-band">
    <h1 class="trip-band__title">SHORT TRIP</h1>
    <div class="trip-band__rule"></div>
  </div>

  <section class="dates">
    <div class="dates__row">
      <p class="dates__label dates__label--early"><strong>Early Bird</strong>Nur bis:</p>
      <div class="dates__field"></div>
    </div>
    <div class="dates__row">
      <p class="dates__label dates__label--second"><strong>Zweiter</strong>Reisezeitraum:</p>
      <div class="dates__field"></div>
    </div>
  </section>

  <blockquote class="testimonial">
    <svg class="testimonial__marks" viewBox="0 0 60 48" aria-hidden="true">
      <path d="M4 4h20v18c0 12-7 20-19 22l-2-6c7-2 10-6 10-12H4z M34 4h20v18c0 12-7 20-19 22l-2-6c7-2 10-6 10-12h-9z" fill="#a2a4aa"/>
    </svg>
    <p class="testimonial__quote">Golferlebnisse, die neue Maßstäbe setzen.</p>
    <cite class="testimonial__cite"><strong>LUKAS BRENNER</strong><span>Golf Professional</span></cite>
  </blockquote>

  <div class="trainer-photo" role="img" aria-label="Porträtfoto des Golftrainers in Schwarzweiß"></div>

  <div class="footer-bar"></div>
</main>
</body>
</html>
```